IT Company Business Card Rebranding

We want to modernize our business cards massively. We want to incorporate aspects of our old business card such as the white and geometric design with the blues of another icon. Existing Logo, old business card and icon are all attached.

We are a modern IT company that provides support for new and growing technologies and want our business cards to be modern yet professional.
Updates

Note: Do not use file ICON.png in design. This is just a design we like Added Wednesday, March 9, 2016

Industry/Entity Type

Information Technology

Contact Information for Business Card

Roughly 43 : 26 or 1075 x 650 px

Font styles to use
Serif

Colors
0492cd
3276b5
33a6d7
86cfc6
cfeae6
cee9f5
ffffff

Requirements
Must have
• Modern yet professional
Nice to have
• We would like to incorporate the blues of our existing logo and of the icon provided. Really like the design of the icon.
Should not have
• Too Decorative. Just simple and professional.
• Not have the circle icon, as it is a copyrighted icon, I just like the colors and the geometric design

```html
<!DOCTYPE html>
<html lang="en">
<head>
<meta charset="utf-8">
<title>Novaridge IT – Business Card</title>
<link href="https://fonts.googleapis.com/css2?family=Play:wght@700&family=Roboto:wght@300;400&display=swap" rel="stylesheet">
<style>
  :root {
    --page-bg: #eceef1;
    --card-bg: #ffffff;
    --frame-light: #33a6d7;
    --frame-dark: #2a3fb8;
    --name-blue: #2d6fd1;
    --text-grey: #6b6f76;
    --logo-grey: #9a9ea5;
    --icon-dark: #3a3f47;
  }
  * { margin: 0; padding: 0; box-sizing: border-box; }
  html, body {
    width: 1200px;
    height: 950px;
    overflow: hidden;
    background: var(--page-bg);
  }
  .stage {
    width: 1200px;
    height: 950px;
    display: flex;
    align-items: center;
    justify-content: center;
  }
  .card {
    position: relative;
    width: 900px;
    height: 544px;
    background: var(--card-bg);
    box-shadow: 0 10px 30px rgba(20, 40, 90, 0.12);
  }
  .card-frame {
    position: absolute;
    inset: 20px;
    border: 2px solid;
    border-image: linear-gradient(20deg, var(--frame-dark), var(--frame-light)) 1;
  }
  .brand {
    position: absolute;
    left: 120px;
    top: 250px;
    display: flex;
    align-items: center;
    gap: 16px;
  }
  .brand-dot {
    width: 22px;
    height: 22px;
    border-radius: 50%;
    background: var(--frame-light);
  }
  .brand-name {
    font-family: "Roboto", sans-serif;
    font-weight: 300;
    font-size: 30px;
    letter-spacing: 8px;
    color: var(--logo-grey);
  }
  .contact {
    position: absolute;
    left: 520px;
    top: 150px;
  }
  .contact-name {
    font-family: "Play", sans-serif;
    font-weight: 700;
    font-size: 34px;
    color: var(--name-blue);
    line-height: 1.1;
  }
  .contact-title {
    font-family: "Roboto", sans-serif;
    font-weight: 400;
    font-size: 19px;
    color: var(--text-grey);
    margin-top: 4px;
  }
  .contact-list {
    list-style: none;
    margin-top: 30px;
  }
  .contact-item {
    display: flex;
    align-items: center;
    gap: 12px;
    font-family: "Roboto", sans-serif;
    font-size: 19px;
    color: var(--text-grey);
    margin-bottom: 9px;
  }
  .contact-icon {
    width: 18px;
    height: 18px;
    flex: none;
  }
</style>
</head>
<body>
<main class="stage">
  <section class="card">
    <div class="card-frame"></div>

    <div class="brand">
      <span class="brand-dot"></span>
      <span class="brand-name">NOVARIDGE IT</span>
    </div>

    <div class="contact">
      <h1 class="contact-name">Daniel Reyes</h1>
      <p class="contact-title">CEO / Founder</p>
      <ul class="contact-list">
        <li class="contact-item">
          <svg class="contact-icon" viewBox="0 0 24 24" aria-hidden="true">
            <path fill="#3a3f47" d="M6.6 10.8a15.1 15.1 0 0 0 6.6 6.6l2.2-2.2c.3-.3.7-.4 1-.2 1.1.4 2.3.6 3.6.6.6 0 1 .4 1 1V20c0 .6-.4 1-1 1A17 17 0 0 1 3 4c0-.6.4-1 1-1h3.5c.6 0 1 .4 1 1 0 1.3.2 2.5.6 3.6.1.3 0 .7-.2 1z"/>
          </svg>
          555 214 7390
        </li>
        <li class="contact-item">
          <svg class="contact-icon" viewBox="0 0 24 24" aria-hidden="true">
            <rect x="2" y="5" width="20" height="14" rx="1.5" fill="#3a3f47"/>
            <path d="M3 6l9 7 9-7" stroke="#ffffff" stroke-width="1.6" fill="none"/>
          </svg>
          hello@novaridge.com
        </li>
        <li class="contact-item">
          <svg class="contact-icon" viewBox="0 0 24 24" aria-hidden="true">
            <circle cx="12" cy="12" r="10" fill="#3a3f47"/>
            <path d="M2 12h20M12 2c3 3 3 17 0 20M12 2c-3 3-3 17 0 20" stroke="#ffffff" stroke-width="1.4" fill="none"/>
          </svg>
          www.novaridge.com
        </li>
      </ul>
    </div>
  </section>
</main>
</body>
</html>
```